Cat-products company needs smart, yet endearing, business card

We need a business card design for a new, but up-and-running, business based in Honolulu, Hawaii. The business is Purrlane Nest Co. Our first product is the most environmentally-friendly cat grass kit ever seen on the planet. Future products, currently in the R&D phase, will include a variety of exciting cat scratchers. We also do consulting work to help apartment-dwellers make their home more cat-friendly and, in the future, plan on doing full, custom installs of structure to create high walkways for cats.

Target Market(s)

Middle-aged, apartment-dwelling, middle-class workers who own 1 or more cats and who dote on them.

Industry/Entity Type

Pet Care

Contact Information for Business Card

A striking, professional, yet warm and friendly design is what we're after.

Font styles to use
Serif
Sans Serif
Other font styles liked:
• Comfortaa

Colors

Designer to choose colors to be used in the design.

Requirements
Must have
• The company logo: (see attachment)
• The company name: Purrlane Nest Co
• The web address: www.purrlanenestco.example
• Email: support@purrlanenestco.example
• Phone: +1 (808) 555 0172
• Update (Fri Jun 30 3017 7:45pm Hawaii Time) I would like, is possible, uploaded picture of the cat grass kit on the back of the card with some text along the lines of: Purrlane Nest Co - Where The Freshest Kitty Sprouts Begin
Nice to have
• A cat picture, cartoon, real or silhouette that illustrates cats in action and/or relaxing; ie using the apartment space to live, play and relax in and being well-contented.
• Most of the website is done in the font: Comfortaa. It might be nice to continue using this for brand consistency.
Should not have
• Hard-to-read fonts.

```html
<!DOCTYPE html>
<html lang="en">
<head>
<meta charset="utf-8">
<title>Purrlane Nest Co – Business Card</title>
<link href="https://fonts.googleapis.com/css2?family=Comfortaa:wght@400;700&family=Quicksand:wght@500;600&display=swap" rel="stylesheet">
<style>
  :root {
    --backdrop: #0b0b0b;
    --paper: #fbf8f2;
    --cocoa: #5a352f;
    --cocoa-ink: #4a2c27;
    --sun: #f8b21c;
    --amber: #e9a12c;
    --rule: #7a5a54;
    --art-dark: #b86a12;
    --art-light: #f3a326;
  }
  * { box-sizing: border-box; margin: 0; padding: 0; }
  html, body {
    width: 1200px; height: 1000px; overflow: hidden;
    background: var(--backdrop);
  }
  .stage {
    position: relative; width: 1200px; height: 1000px;
    display: flex; flex-direction: column; align-items: center; justify-content: center; gap: 60px;
  }
  .card {
    position: relative; width: 560px; height: 320px; overflow: hidden;
    box-shadow: 0 10px 30px rgba(0,0,0,.6);
  }

  /* Front */
  .card-front { background: var(--paper); }
  .card-front .accent-band {
    position: absolute; left: 0; right: 0; bottom: 0; height: 16px; background: var(--sun);
  }
  .brand {
    position: absolute; left: 40px; top: 132px;
    display: flex; align-items: center; gap: 10px;
  }
  .brand-mark { width: 18px; height: 18px; background: var(--cocoa); }
  .brand-name {
    font-family: 'Comfortaa', sans-serif; font-weight: 700; font-size: 19px; color: var(--cocoa);
    white-space: nowrap;
  }
  .divider {
    position: absolute; left: 262px; top: 50px; bottom: 66px; width: 14px;
    display: flex; flex-direction: column; align-items: center; gap: 14px;
  }
  .divider .rule { flex: 1; width: 1.5px; background: var(--rule); }
  .divider .dot { width: 14px; height: 14px; border-radius: 50%; background: var(--cocoa); }
  .contact {
    position: absolute; left: 310px; top: 82px; color: var(--cocoa-ink);
    font-family: 'Quicksand', sans-serif; white-space: nowrap;
  }
  .contact .person {
    font-family: 'Comfortaa', sans-serif; font-size: 25px; color: var(--sun); line-height: 1.1;
  }
  .contact .role { font-size: 15px; font-weight: 600; margin-bottom: 26px; }
  .contact .line { font-size: 13px; font-weight: 600; line-height: 1.55; }

  /* Back */
  .card-back { background: var(--cocoa); }
  .card-back svg { display: block; }
</style>
</head>
<body>
<main class="stage">
  <section class="card card-front" aria-label="Business card front">
    <div class="brand">
      <span class="brand-mark"></span>
      <span class="brand-name">Purrlane Nest Co</span>
    </div>
    <div class="divider" aria-hidden="true">
      <span class="rule"></span><span class="dot"></span><span class="rule"></span>
    </div>
    <div class="contact">
      <p class="person">Leilani Kahale</p>
      <p class="role">Manager</p>
      <p class="line">+1 (808) 555 0172</p>
      <p class="line">support@purrlanenestco.example</p>
      <p class="line">www.purrlanenestco.example</p>
    </div>
    <div class="accent-band"></div>
  </section>

  <section class="card card-back" aria-label="Business card back">
    <svg width="560" height="320" viewBox="0 0 560 320">
      <defs>
        <linearGradient id="art-tones" x1="0" y1="0" x2="1" y2="1">
          <stop offset="0" stop-color="var(--art-light)"/>
          <stop offset="1" stop-color="var(--art-dark)"/>
        </linearGradient>
      </defs>
      <polygon points="0,0 170,0 0,150" fill="var(--amber)"/>
      <polygon points="0,150 170,0 176,0 4,156" fill="var(--paper)"/>
      <polygon points="0,156 0,320 150,320" fill="var(--sun)"/>
      <rect x="540" y="0" width="20" height="320" fill="var(--paper)"/>
      <rect class="feature-art" role="img"
            aria-label="Illustration area: paw print with a heart-shaped photo of a cat silhouette against a sunset sky"
            x="195" y="40" width="250" height="250" rx="16"
            fill="url(#art-tones)"/>
    </svg>
  </section>
</main>
</body>
</html>
```